Brisk Tide needs a web page for E-commerce site

Small startup business looking for a custom website for my New Saltwater apparel Co.

COMPANY OVERVIEW

Brisk Tide was founded In Mont Belvieu, Tx, right on the heart of pelican cove.

Brisk Tide is the adrenaline, sweat pumping moment you find yourself setting the hook on a monster fish. This is the moment when all your senses come to life as you work to land that trophy, and after a grueling fight when your hi-fiving your fishing buddies...It's that moment... when the waters and the air around you are Brisk Sweet....All or Nothing...pure Addiction......This is BRISK TIDE

Looking for a sharp clean sexy web page for my ecommerce page

I like the look of black background websites.

www.brisktidegear.example
Updates

I am using bigcommerce as my host site if that means anything to y'all

Thank you all for the submissions! There were some great ones!  I will have more projects in the future. thanks again

Target Market(s)

inshore/offshore fishing, saltwater enthusiast

Industry/Entity Type

Business

Requirements
Must have
• logo's

inshore/offshore fishing appeal

compatible with bigcommerce site

```html
<!DOCTYPE html>
<html lang="en">
<head>
<meta charset="utf-8">
<title>Brisk Tide — Saltwater Apparel Shop</title>
<link rel="stylesheet" href="https://fonts.googleapis.com/css2?family=Questrial&family=Delius&family=Abril+Fatface&family=Black+Ops+One&family=Open+Sans:wght@400;600&display=swap">
<style>
  :root {
    --page-dark: #050607;
    --page-side: #14171a;
    --panel-top: #0b0f13;
    --panel-mid: #0d1b26;
    --panel-low: #070b0f;
    --panel-deep: #030405;
    --ocean-glow: rgba(20,110,160,.45);
    --logo-fill: #0f5f86;
    --accent: #19a7d1;
    --accent-bright: #2cc4ec;
    --button: #137fa8;
    --ink-light: #9fd8ec;
    --white: #ffffff;
    --soft-white: #dfeef4;
    --line: #1d6f92;
  }
  * { box-sizing: border-box; margin: 0; padding: 0; }
  html, body { width: 1200px; height: 1025px; overflow: hidden; }
  body {
    position: relative;
    background: radial-gradient(ellipse at center, var(--page-side) 0%, var(--page-dark) 85%);
    font-family: "Questrial", sans-serif;
    color: var(--white);
  }
  .page {
    position: absolute; left: 148px; top: 0; width: 903px; height: 1025px;
    background:
      radial-gradient(ellipse 70% 40% at 55% 38%, var(--ocean-glow), transparent 70%),
      linear-gradient(180deg, var(--panel-top) 0%, var(--panel-mid) 40%, var(--panel-low) 70%, var(--panel-deep) 100%);
  }
  .abs { position: absolute; }

  .account-links { left: 604px; top: 8px; font-size: 11px; white-space: nowrap; }
  .search { left: 665px; top: 36px; width: 216px; height: 29px; display: flex; }
  .search-field { width: 152px; height: 29px; background: var(--white); }
  .search-button { width: 64px; height: 29px; background: var(--button); color: var(--white);
    font: 13px "Open Sans", sans-serif; display: flex; align-items: center; justify-content: center; }

  .latest { left: 37px; top: 48px; font: 11px "Open Sans", sans-serif; white-space: nowrap; }
  .logo { left: 32px; top: 70px; width: 339px; height: 129px; background: var(--logo-fill);
    display: flex; align-items: center; justify-content: center;
    font-family: "Questrial", sans-serif; font-size: 46px; color: var(--white); letter-spacing: 2px; }

  .main-nav { left: 372px; top: 124px; width: 509px; height: 44px; background: #000; font-size: 14px; letter-spacing: .3px; }
  .main-nav span { position: absolute; top: 14px; }

  .hero-year { left: 90px; top: 236px; font-family: "Abril Fatface", serif; font-size: 62px; letter-spacing: 2px; line-height: 1; }
  .hero-designer { left: 32px; top: 318px; font-family: "Black Ops One", sans-serif; font-size: 40px;
    color: var(--ink-light); letter-spacing: 2px; line-height: 1; }
  .hero-collections { left: 178px; top: 390px; font-size: 27px; letter-spacing: -.5px; line-height: 1; }
  .hero-arrow { left: 345px; top: 376px; }
  .hero-photo { left: 394px; top: 207px; width: 480px; height: 221px;
    background: linear-gradient(100deg, #0d4a6b, #2b89b0 45%, #7cc6de 70%, #1b5d7e); }

  .categories { left: 40px; top: 482px; width: 831px; height: 336px;
    border: 1px solid var(--line); background: rgba(0,0,0,.35); }
  .categories-title { left: 58px; top: 492px; font-family: "Delius", cursive; font-size: 22px; font-weight: 400; color: var(--accent-bright); }
  .category-image { border-radius: 6px; }
  .img-clothing { left: 81px; top: 554px; width: 202px; height: 205px;
    background: linear-gradient(160deg, #1e4f6e, #4f8fb0 60%, #163a52); }
  .img-accessories { left: 370px; top: 529px; width: 197px; height: 230px;
    background: linear-gradient(160deg, #6b6f74, #a9b0b6 55%, #3d4247); }
  .img-footwear { left: 610px; top: 542px; width: 193px; height: 200px;
    background: linear-gradient(160deg, #2a2a2c, #6e6e72 50%, #111); }
  .category-label { top: 771px; width: 200px; text-align: center; font-family: "Delius", cursive; font-size: 19px; }
  .arrow-left { left: 19px; top: 603px; }
  .arrow-right { left: 861px; top: 603px; }

  .divider { left: 29px; top: 844px; width: 846px; height: 1px; background: var(--soft-white); }
  .quick-link { font-family: "Delius", cursive; font-size: 14px; display: flex; align-items: center; gap: 17px; }
  .quick-icon { width: 15px; height: 15px; border-radius: 3px; background: var(--accent-bright);
    box-shadow: 0 0 6px 2px rgba(44,196,236,.6); }

  .site-footer { left: 6px; top: 953px; width: 893px; height: 51px; background: rgba(0,0,0,.6); }
  .footer-links { top: 961px; font: 10.5px "Open Sans", sans-serif; white-space: nowrap; }
  .copyright { left: 54px; top: 983px; font: 10.5px "Open Sans", sans-serif; }
</style>
</head>
<body>
<div class="page">
  <div class="abs account-links">My Account | View Cart &nbsp;| Sign in or Create an account</div>
  <div class="abs search"><div class="search-field"></div><div class="search-button">Search</div></div>

  <div class="abs latest">LATEST PROJECT: Online Shopping Sites In -------------</div>
  <div class="abs logo">BRISK TIDE</div>

  <nav class="abs main-nav">
    <span style="left:21px">LADIES</span>
    <span style="left:101px">MENS</span>
    <span style="left:181px">SALES</span>
    <span style="left:260px">ACCESORIES</span>
    <span style="left:383px">ORDER STATUS</span>
  </nav>

  <div class="abs hero-year">2013</div>
  <div class="abs hero-designer">OFFSHORE</div>
  <div class="abs hero-collections">COLLECTIONS</div>
  <svg class="abs hero-arrow" width="30" height="62" viewBox="0 0 30 62"><polyline points="3,2 27,31 3,60" fill="none" stroke="#2cc4ec" stroke-width="3"/></svg>
  <div class="abs hero-photo" role="img" aria-label="Anglers on open saltwater wearing the new season's performance fishing shirts"></div>

  <section class="abs categories"></section>
  <h2 class="abs categories-title">Products Categories</h2>
  <svg class="abs arrow-left" width="30" height="62" viewBox="0 0 30 62"><polyline points="27,2 3,31 27,60" fill="none" stroke="#2cc4ec" stroke-width="2.5"/></svg>
  <svg class="abs arrow-right" width="30" height="62" viewBox="0 0 30 62"><polyline points="3,2 27,31 3,60" fill="none" stroke="#2cc4ec" stroke-width="2.5"/></svg>
  <div class="abs category-image img-clothing" role="img" aria-label="Long-sleeve sun-protection fishing shirt and tee"></div>
  <div class="abs category-image img-accessories" role="img" aria-label="Fishing cap, buff and waterproof tackle bag"></div>
  <div class="abs category-image img-footwear" role="img" aria-label="Non-slip deck boots"></div>
  <div class="abs category-label" style="left:117px">Clothing</div>
  <div class="abs category-label" style="left:372px">Accessories</div>
  <div class="abs category-label" style="left:642px">Footwear</div>

  <div class="abs divider"></div>

  <div class="abs quick-link" style="left:69px;top:870px"><span class="quick-icon"></span>Shirts</div>
  <div class="abs quick-link" style="left:279px;top:870px"><span class="quick-icon"></span>Hats</div>
  <div class="abs quick-link" style="left:485px;top:870px"><span class="quick-icon"></span>Tackle Bags</div>
  <div class="abs quick-link" style="left:714px;top:870px"><span class="quick-icon"></span>Footwears</div>
  <div class="abs quick-link" style="left:69px;top:907px"><span class="quick-icon"></span>Inshore</div>
  <div class="abs quick-link" style="left:279px;top:907px"><span class="quick-icon"></span>Offshore</div>
  <div class="abs quick-link" style="left:485px;top:907px"><span class="quick-icon"></span>Sun Gear</div>
  <div class="abs quick-link" style="left:714px;top:907px"><span class="quick-icon"></span>Deck Boots</div>

  <footer class="abs site-footer"></footer>
  <div class="abs footer-links" style="left:54px">About Us</div>
  <div class="abs footer-links" style="left:118px">Customer Service</div>
  <div class="abs footer-links" style="left:216px">Site Map</div>
  <div class="abs footer-links" style="left:282px">Search Terms &nbsp;Advanced Search</div>
  <div class="abs footer-links" style="left:444px">Contact Us</div>
  <div class="abs copyright">© 2013 BRISK TIDE. All Rights Reserved.</div>
</div>
</body>
</html>
```